Business Postcard Mailer - 2 sided - 6 x 10.5 inches

We will be purchasing multiple designs through this project. We need a postcard mailer for a residential painting business. The final design needs to have the special 15% Off, contact information, company logo, stamp indicia, and list of services. I will provide past examples and any additional logos. Company colors are #34482E and #4A1717. Old samples are provided. Final flat size should be 6 x 10.5 inches. And we will need a return address in the upper left-hand corner of the backside. QMRB Layout Guidelines are attached. 4389 Juniper Ave #7, Waukesha, WI 53947.
Updates

I just guaranteed the project and will be expecting more entries. We will also be purchasing additional designs (4-5) so we want to ensure a good variety.

Target Market(s)

Homeowners

Industry/Entity Type

Painting

Font styles to use
Sans Serif

Requirements
Must have
• Logo and brand colors
Nice to have
• Call to action - Book your free estimate at www.BrightCoatCrew.example or Call now 262-555-0147.

```html
<!DOCTYPE html>
<html lang="en">
<head>
<meta charset="utf-8">
<title>Bright Coat Crew Postcard</title>
<link rel="stylesheet" href="https://fonts.googleapis.com/css2?family=Arimo:ital,wght@0,400;0,700;1,700&family=Oswald:wght@500;600&display=swap">
<style>
:root{
  --green:#34482E;
  --maroon:#4A1717;
  --white:#ffffff;
  --grey:#8e9a8a;
  --badge:#cfcfcf;
  --ink:#1d1d1d;
}
*{margin:0;padding:0;box-sizing:border-box}
html,body{width:686px;height:1200px;overflow:hidden;background:var(--white)}
.card{position:relative;width:686px;height:1200px;font-family:"Arimo",Arial,sans-serif;background:var(--white);overflow:hidden}
.abs{position:absolute}
.brand{left:10px;top:12px;width:300px}
.brand-name{display:flex;align-items:flex-start;gap:10px;font-weight:700;font-size:38px;line-height:42px;color:var(--green)}
.brand-mark{width:26px;height:26px;background:var(--maroon);margin-top:9px;flex:none}
.brand-address{position:absolute;left:0;top:104px;white-space:nowrap;font-weight:700;font-size:21px;line-height:38px;color:var(--maroon)}
.indicia{left:316px;top:26px;width:101px;height:101px;border:2px solid var(--ink);text-align:center;font-size:12px;line-height:15px;color:var(--ink);padding-top:5px}
.indicia .paid{font-weight:700;font-size:15px;border-top:1px solid var(--ink);border-bottom:1px solid var(--ink);margin:3px 8px;line-height:19px}
.special{left:445px;top:0;width:241px;height:194px;background:var(--maroon);color:var(--white);font-family:"Oswald",Arial,sans-serif;text-align:center}
.special-title{font-size:40px;font-weight:500;margin-top:24px;line-height:1.1}
.special-offer{font-size:62px;font-weight:600;margin-top:8px;line-height:1.1}
.middle{left:0;top:194px;width:686px;height:826px;background:var(--green)}
.frame-tail{left:381px;top:1020px;width:305px;height:44px;background:var(--green)}
.strip-maroon{background:var(--maroon)}
.panel{background:var(--white);left:0;width:380px}
.services{top:210px;height:256px;overflow:hidden}
.services-watermark{position:absolute;left:22px;top:187px;font-size:68px;line-height:68px;font-weight:700;color:var(--grey);opacity:.85;transform:rotate(-33deg);transform-origin:left bottom;white-space:nowrap}
.service-list{position:relative;list-style:none;padding:19px 0 0 22px}
.service-list li{display:flex;align-items:center;gap:6px;font-weight:700;font-style:italic;font-size:31px;color:var(--maroon);height:47px;white-space:nowrap}
.brush{width:8px;height:32px;flex:none}
.tagline{top:483px;height:227px;display:flex;align-items:center;justify-content:center;text-align:center;font-weight:700;font-style:italic;font-size:30px;line-height:41.5px;color:var(--green);white-space:nowrap}
.badges{top:725px;height:280px}
.badge{position:absolute;background:var(--badge);border-radius:6px}
.photo{left:393px;width:286px}
.contact-row{position:absolute;left:18px;display:flex;align-items:center;gap:18px;font-weight:700;color:var(--maroon);white-space:nowrap;line-height:1}
.contact-row svg{flex:none}
.phone{top:1030px;height:44px;font-size:44px}
.web{top:1096px;height:40px;font-size:35px}
.email{top:1156px;height:40px;font-size:35px}
</style>
</head>
<body>
<div class="card">
  <div class="abs brand">
    <div class="brand-name"><span class="brand-mark"></span><span>Bright Coat<br>Crew</span></div>
    <div class="brand-address">4389 JUNIPER AVE #7,<br>WAUKESHA, WI 53947</div>
  </div>

  <div class="abs indicia">
    Presorted<br>Standard<br>QMRB Postage
    <div class="paid">PAID</div>
    PMX
  </div>

  <div class="abs special">
    <div class="special-title">The Special</div>
    <div class="special-offer">15% OFF</div>
  </div>

  <div class="abs middle"></div>
  <div class="abs frame-tail"></div>
  <div class="abs strip-maroon" style="left:0;top:466px;width:393px;height:17px"></div>
  <div class="abs strip-maroon" style="left:380px;top:345px;width:13px;height:190px"></div>
  <div class="abs strip-maroon" style="left:679px;top:530px;width:7px;height:200px"></div>

  <section class="abs panel services">
    <div class="services-watermark">SERVICES</div>
    <ul class="service-list">
      <li><svg class="brush" viewBox="0 0 8 32"><rect x="0" y="0" width="8" height="12" rx="2" fill="#34482E"/><rect x="2.5" y="12" width="3" height="20" fill="#4A1717"/></svg>Interior Painting</li>
      <li><svg class="brush" viewBox="0 0 8 32"><rect x="0" y="0" width="8" height="12" rx="2" fill="#34482E"/><rect x="2.5" y="12" width="3" height="20" fill="#4A1717"/></svg>Exterior Painting</li>
      <li><svg class="brush" viewBox="0 0 8 32"><rect x="0" y="0" width="8" height="12" rx="2" fill="#34482E"/><rect x="2.5" y="12" width="3" height="20" fill="#4A1717"/></svg>Carpentry Services</li>
      <li><svg class="brush" viewBox="0 0 8 32"><rect x="0" y="0" width="8" height="12" rx="2" fill="#34482E"/><rect x="2.5" y="12" width="3" height="20" fill="#4A1717"/></svg>Drywall Repair</li>
      <li><svg class="brush" viewBox="0 0 8 32"><rect x="0" y="0" width="8" height="12" rx="2" fill="#34482E"/><rect x="2.5" y="12" width="3" height="20" fill="#4A1717"/></svg>Color Consultations</li>
    </ul>
  </section>

  <section class="abs panel tagline">
    <p>We cater the size of the<br>crew to the size of the<br>job and work full<br>continuous days until<br>the project is complete.</p>
  </section>

  <section class="abs panel badges" aria-label="Membership badges">
    <div class="badge" style="left:18px;top:50px;width:118px;height:125px"></div>
    <div class="badge" style="left:150px;top:35px;width:105px;height:68px"></div>
    <div class="badge" style="left:258px;top:30px;width:105px;height:108px"></div>
    <div class="badge" style="left:110px;top:120px;width:105px;height:50px"></div>
    <div class="badge" style="left:240px;top:155px;width:110px;height:42px"></div>
    <div class="badge" style="left:18px;top:185px;width:186px;height:70px"></div>
    <div class="badge" style="left:215px;top:212px;width:142px;height:48px"></div>
  </section>

  <div class="abs photo" style="top:210px;height:166px;background:linear-gradient(135deg,#f2c12e,#f7f3e8 60%,#d9d4cb)" role="img" aria-label="Bright home office with a yellow accent wall and a desk"></div>
  <div class="abs photo" style="top:389px;height:212px;background:linear-gradient(90deg,#ecebe6 50%,#5e8fb0 55%,#6b97b6)" role="img" aria-label="Room wall half painted blue with a ladder and paint can"></div>
  <div class="abs photo" style="top:614px;height:214px;background:linear-gradient(160deg,#f4f4f2,#cfd9e6 55%,#7fa9d8)" role="img" aria-label="Painter spraying a white porch railing"></div>
  <div class="abs photo" style="top:840px;height:213px;background:linear-gradient(180deg,#f3efe6,#e5dccb 70%,#c9a77d)" role="img" aria-label="Freshly painted living room with a white fireplace"></div>

  <div class="contact-row phone">
    <svg width="40" height="38" viewBox="0 0 34 38"><path d="M6 3l7 0 3 9-4 3c2 5 5 9 9 11l3-4 9 3 0 7c-1 3-4 4-7 3C14 32 5 22 3 9 2 6 3 3 6 3z" fill="#1d1d1d"/></svg>
    262-555-0147
  </div>
  <div class="contact-row web">
    <svg width="40" height="32" viewBox="0 0 40 32"><rect x="2" y="2" width="36" height="22" rx="2" fill="none" stroke="#1d1d1d" stroke-width="3"/><rect x="6" y="6" width="28" height="14" fill="#1d1d1d"/><rect x="0" y="26" width="40" height="4" fill="#1d1d1d"/></svg>
    www.BrightCoatCrew.example
  </div>
  <div class="contact-row email">
    <svg width="40" height="32" viewBox="0 0 40 32"><rect x="2" y="4" width="36" height="26" fill="none" stroke="#1d1d1d" stroke-width="3"/><path d="M2 4l18 15 18-15" fill="none" stroke="#1d1d1d" stroke-width="3"/></svg>
    hello@BrightCoatCrew.example
  </div>
</div>
</body>
</html>
```